Design a LinkedIn Banner for Company & Sales Reps

Task Description:
We are looking for a talented designer to create a modern, eye-catching LinkedIn banner that will be used on our company LinkedIn page, as well as by our sales reps on their individual LinkedIn profiles.
Key Requirements:
Clean, sharp, and professional design
Must include both the TORALIN logo (primary) and the ORBA CALM RX logo (secondary)
We would like two separate color versions of the same banner:
One that matches TORALIN brand colors
One that matches ORBA CALM RX brand colors
Layout and design elements can remain the same between both versions — only the color palette should differ
Design Style:
Simple yet sharp and modern
Professional and clean — not overly busy
Visually balanced to highlight both brands appropriately
Target Market(s)
Medical Device Industry & Physicians
Industry/Entity Type
Medical Device / Pain Management
Look and feel

```html
<!DOCTYPE html>
<html lang="en">
<head>
<meta charset="UTF-8">
<title>TORALIN LinkedIn Banner</title>
<link href="https://fonts.googleapis.com/css2?family=Barlow+Semi+Condensed:wght@300;400;500&display=swap" rel="stylesheet">
<style>
  :root {
    --green: #6cb94a;
    --ink: #1d1d1f;
    --muted: #3a3a3c;
    --navy: #1f2c5c;
    --teal-deep: #17867c;
    --teal-mid: #3fb3a6;
    --teal-light: #a9e3da;
    --paper: #ffffff;
  }
  * { box-sizing: border-box; margin: 0; padding: 0; }
  html, body { width: 1200px; height: 300px; overflow: hidden; background: var(--paper); }
  .banner {
    position: relative;
    width: 1200px;
    height: 300px;
    background: var(--paper);
    font-family: "Barlow Semi Condensed", "Arial Narrow", sans-serif;
    color: var(--ink);
    overflow: hidden;
  }
  .edge-bar {
    position: absolute; left: 0; top: 0;
    width: 5px; height: 100%;
    background: var(--green);
  }
  .brand-name {
    position: absolute; left: 51px; top: 34px;
    font-size: 44px; font-weight: 300; letter-spacing: 1px;
    color: var(--green); line-height: 1;
  }
  .tagline {
    position: absolute; left: 50px; top: 208px;
    font-size: 15px; font-weight: 300; letter-spacing: -0.3px;
    color: var(--muted);
  }
  .cta {
    position: absolute; left: 51px; top: 241px;
    width: 132px; height: 29px;
    border: 1px solid var(--green); border-radius: 15px;
    display: flex; align-items: center; justify-content: center; gap: 8px;
    font-size: 12px; font-weight: 400; color: var(--ink);
    text-decoration: none;
  }
  .cta svg { width: 13px; height: 8px; }
  .divider {
    position: absolute; left: 554px; top: 57px;
    width: 1px; height: 188px;
    background: var(--green);
  }
  .mission {
    position: absolute; left: 600px; top: 62px;
    width: 360px;
    font-size: 24px; font-weight: 400; line-height: 38px;
    color: var(--ink);
  }
  .helix-visual {
    position: absolute; left: 1020px; top: 0;
    width: 160px; height: 300px;
    background:
      radial-gradient(ellipse 40% 30% at 60% 8%, var(--teal-deep), transparent 70%),
      radial-gradient(ellipse 45% 30% at 50% 45%, var(--teal-mid), transparent 72%),
      radial-gradient(ellipse 50% 35% at 40% 88%, var(--teal-light), transparent 75%);
  }
  .partner-badge {
    position: absolute; left: 1103px; top: 254px;
    width: 88px; height: 44px;
    background: rgba(255,255,255,0.92);
    border-radius: 5px;
    display: flex; align-items: center; justify-content: center;
    font-size: 13px; font-weight: 500; letter-spacing: 0.3px;
    color: var(--navy);
  }
</style>
</head>
<body>
  <div class="banner">
    <div class="edge-bar"></div>
    <div class="brand-name">TORALIN</div>
    <p class="tagline">Extracellular-matrix science meets minimally invasive implants</p>
    <a class="cta" href="#">Explore at toralin.com
      <svg viewBox="0 0 13 8" aria-hidden="true"><path d="M0 4h12M8.5 0.8L12 4 8.5 7.2" fill="none" stroke="#1d1d1f" stroke-width="1"/></svg>
    </a>
    <div class="divider"></div>
    <p class="mission">“Our mission is to provide advanced regenerative product solutions that help patients suffering from musculoskeletal injuries, wounds, and burned skin.”</p>
    <div class="helix-visual" role="img" aria-label="Teal DNA double helix illustration"></div>
    <div class="partner-badge">ORBA CALM RX</div>
  </div>
</body>
</html>
```